Brightwell Spray Foam Post cards

Looking to build a brand with mass mail out post cards. need somthing that represents our trailer designs, and facebook but gives enough info for the clients to call us

```html
<!DOCTYPE html>
<html lang="en">
<head>
<meta charset="utf-8">
<title>Brightwell Spray Foam Postcards</title>
<link href="https://fonts.googleapis.com/css2?family=Montserrat:wght@700;800&family=Roboto:wght@400&display=swap" rel="stylesheet">
<style>
  :root{
    --stage:#9a9a9a;
    --navy:#1c3a8c;
    --royal:#2b55b0;
    --sky:#2a94dc;
    --ink:#111318;
    --white:#ffffff;
    --panel:#dadada;
    --icon-light:#9cc2f0;
  }
  html,body{margin:0;padding:0;}
  body{width:1200px;height:687px;overflow:hidden;background:var(--stage);position:relative;}
  .postcard{position:absolute;top:185px;width:412px;height:317px;}
  .postcard--front{left:162px;}
  .postcard--back{left:624px;}
  .postcard svg{display:block;width:100%;height:100%;}
  .heading{font-family:"Montserrat",sans-serif;font-weight:700;fill:var(--white);}
  .brand{font-family:"Montserrat",sans-serif;font-weight:800;fill:var(--white);letter-spacing:1px;}
  .contact{font-family:"Roboto",sans-serif;font-weight:400;fill:var(--white);font-size:10.5px;}
  .contact--small{font-size:8.5px;}
</style>
</head>
<body>

<div class="postcard postcard--front">
  <svg viewBox="0 0 515 396" xmlns="http://www.w3.org/2000/svg">
    <defs>
      <linearGradient id="frontBlue" x1="0" y1="0" x2="0" y2="1">
        <stop offset="0" stop-color="#223f93"/>
        <stop offset="0.6" stop-color="#2e59b6"/>
        <stop offset="1" stop-color="#1f3d8e"/>
      </linearGradient>
      <linearGradient id="frontPhoto" x1="0" y1="0" x2="0" y2="1">
        <stop offset="0" stop-color="#9aa2b0"/>
        <stop offset="0.5" stop-color="#6e7686"/>
        <stop offset="1" stop-color="#a5adb9"/>
      </linearGradient>
    </defs>
    <rect class="card-base" width="515" height="396" fill="url(#frontBlue)"/>

    <path class="wave wave--dark" d="M338,0 C318,90 270,150 286,230 C296,290 300,330 296,396 H515 V0 Z" fill="var(--ink)"/>
    <path class="wave wave--sky" d="M348,0 C330,90 284,150 300,230 C310,290 312,330 308,396 H515 V0 Z" fill="var(--sky)"/>
    <path class="attic-photo" role="img" aria-label="Photo of an attic roof sprayed with insulation foam between timber rafters"
          d="M360,0 H515 V396 H318 C322,320 314,280 310,230 C300,160 342,90 360,0 Z" fill="url(#frontPhoto)"/>
    <path class="arc arc--sky" d="M300,290 C360,230 440,205 515,210" fill="none" stroke="var(--sky)" stroke-width="6"/>

    <text class="heading" x="164" y="42" font-size="14" text-anchor="middle">DFW PREMIER INSULATION COMPANY</text>
    <line x1="22" y1="60" x2="305" y2="60" stroke="var(--white)" stroke-width="1.5"/>
    <text class="brand" x="164" y="78" font-size="16" text-anchor="middle">BRIGHTWELL</text>
    <text class="brand" x="164" y="98" font-size="16" text-anchor="middle">SPRAY FOAM</text>
    <line x1="22" y1="105" x2="305" y2="105" stroke="var(--white)" stroke-width="1.5"/>

    <g class="service-list heading" font-size="16.5" text-anchor="middle">
      <text x="145" y="145">SPRAY FOAM</text>
      <text x="145" y="179">FIBERGLASS</text>
      <text x="145" y="213">INSULATION</text>
      <text x="145" y="248">ROOFING</text>
    </g>
    <g stroke="#7fa6e0" stroke-width="1">
      <line x1="48" y1="155" x2="242" y2="155"/>
      <line x1="48" y1="189" x2="242" y2="189"/>
      <line x1="48" y1="223" x2="242" y2="223"/>
    </g>

    <rect class="tagline-band" x="0" y="269" width="300" height="70" fill="#24449c"/>
    <text class="heading" x="134" y="300" font-size="17.5" text-anchor="middle">ALL ABOUT SPRAY</text>
    <text class="heading" x="134" y="321" font-size="17.5" text-anchor="middle">POLYURETHANE FOAM</text>

    <rect class="contact-band" x="0" y="339" width="300" height="57" fill="var(--ink)"/>
    <polygon class="web-band" points="292,366 515,366 515,396 275,396" fill="var(--sky)"/>

    <g class="icon-phone" fill="var(--white)" transform="translate(24,355)">
      <rect x="0" y="2" width="11" height="7" rx="2"/>
      <rect x="3" y="0" width="5" height="3" rx="1"/>
    </g>
    <text class="contact" x="43" y="364">469-555-0187</text>
    <g class="icon-mail" transform="translate(118,356)">
      <rect width="11" height="8" fill="var(--white)"/>
      <polyline points="0,0 5.5,5 11,0" fill="none" stroke="var(--ink)" stroke-width="1"/>
    </g>
    <text class="contact" x="135" y="364">info@brightwellfoam.com</text>
    <path class="icon-pin" d="M29,372 a4,4 0 0 1 4,4 c0,3 -4,7 -4,7 c0,0 -4,-4 -4,-7 a4,4 0 0 1 4,-4 z" fill="var(--white)"/>
    <text class="contact" x="43" y="381">2200 Ridgeway Dr. Suite 4 Plano, TX 75074</text>

    <circle class="icon-globe" cx="297" cy="378" r="4.5" fill="none" stroke="var(--white)" stroke-width="1.3"/>
    <text class="contact" x="309" y="382">brightwellfoam.com</text>
    <circle class="icon-social" cx="414" cy="378" r="5" fill="var(--white)"/>
    <text class="contact" x="428" y="382">brightwellfoam</text>
  </svg>
</div>

<div class="postcard postcard--back">
  <svg viewBox="0 0 515 396" xmlns="http://www.w3.org/2000/svg">
    <defs>
      <linearGradient id="backTop" x1="0" y1="0" x2="0" y2="1">
        <stop offset="0" stop-color="#2c8fd8"/>
        <stop offset="1" stop-color="#2460bd"/>
      </linearGradient>
      <linearGradient id="backBlue" x1="0" y1="0" x2="0" y2="1">
        <stop offset="0" stop-color="#2a59b8"/>
        <stop offset="1" stop-color="#1d3a8c"/>
      </linearGradient>
      <linearGradient id="backPhoto" x1="0" y1="0" x2="1" y2="1">
        <stop offset="0" stop-color="#a4abb8"/>
        <stop offset="1" stop-color="#4a5364"/>
      </linearGradient>
    </defs>
    <rect class="mail-area" width="515" height="396" fill="var(--panel)"/>
    <rect class="mail-area mail-area--light" x="388" y="0" width="127" height="126" fill="#e4e4e4"/>
    <rect class="body-panel" x="0" y="120" width="250" height="276" fill="url(#backBlue)"/>
    <rect class="header-panel" x="0" y="0" width="388" height="126" fill="url(#backTop)"/>

    <text class="heading" x="175" y="36" font-size="14" text-anchor="middle">DFW PREMIER INSULATION COMPANY</text>
    <line x1="32" y1="53" x2="315" y2="53" stroke="var(--white)" stroke-width="1.5"/>
    <text class="brand" x="173" y="71" font-size="16" text-anchor="middle">BRIGHTWELL</text>
    <text class="brand" x="173" y="91" font-size="16" text-anchor="middle">SPRAY FOAM</text>
    <line x1="32" y1="98" x2="315" y2="98" stroke="var(--white)" stroke-width="1.5"/>

    <g class="tick-list">
      <g fill="none" stroke="var(--icon-light)" stroke-width="1.3">
        <rect x="36" y="134" width="11" height="11"/><polyline points="38,139 41,143 49,132"/>
        <rect x="36" y="158" width="11" height="11"/><polyline points="38,163 41,167 49,156"/>
        <rect x="36" y="182" width="11" height="11"/><polyline points="38,187 41,191 49,180"/>
        <rect x="36" y="207" width="11" height="11"/><polyline points="38,212 41,216 49,205"/>
      </g>
      <g class="heading" font-size="17">
        <text x="63" y="146">SPRAY FOAM</text>
        <text x="63" y="170">FIBERGLASS</text>
        <text x="63" y="194">INSULATION</text>
        <text x="63" y="219">ROOFING</text>
      </g>
    </g>

    <rect class="tagline-band" x="0" y="247" width="250" height="67" fill="var(--ink)"/>
    <text class="heading" x="111" y="268" font-size="14.5" text-anchor="middle">ALL ABOUT SPRAY</text>
    <text class="heading" x="111" y="283" font-size="14.5" text-anchor="middle">POLYURETHANE FOAM</text>
    <text class="contact" x="111" y="299" text-anchor="middle">www.brightwellsprayfoam.net</text>

    <circle class="photo-shadow" cx="253" cy="220" r="52" fill="var(--ink)"/>
    <circle class="photo-ring" cx="248" cy="215" r="52" fill="var(--white)"/>
    <circle class="interior-photo" role="img" aria-label="Photo of an insulated interior wall and doorway" cx="248" cy="215" r="48" fill="url(#backPhoto)"/>

    <g class="contact-block">
      <rect x="22" y="344" width="9" height="6" rx="1.5" fill="var(--icon-light)"/>
      <text class="contact contact--small" x="38" y="350">469-555-0187</text>
      <g transform="translate(101,344)">
        <rect width="9" height="6" fill="var(--icon-light)"/>
        <polyline points="0,0 4.5,3.5 9,0" fill="none" stroke="var(--navy)" stroke-width="0.8"/>
      </g>
      <text class="contact contact--small" x="116" y="350">info@brightwellfoam.com</text>
      <path d="M26,356 a3.5,3.5 0 0 1 3.5,3.5 c0,2.5 -3.5,6 -3.5,6 c0,0 -3.5,-3.5 -3.5,-6 a3.5,3.5 0 0 1 3.5,-3.5 z" fill="var(--icon-light)"/>
      <text class="contact contact--small" x="38" y="364">2200 Ridgeway Dr. Suite 4 Plano, TX 75074</text>
      <circle cx="26" cy="375" r="3.5" fill="var(--icon-light)"/>
      <text class="contact contact--small" x="38" y="378">brightwellfoam.com</text>
      <circle cx="128" cy="375" r="4" fill="var(--icon-light)"/>
      <text class="contact contact--small" x="137" y="378">brightwellfoam</text>
    </g>
  </svg>
</div>

</body>
</html>
```